Business card for web design company
Web. Graphics. Print
Business card for web design company - Communications and Media
Creative Brief
Simple
Lunar Orchard
None
tessa@lunarorchard.example
www.lunarorchard.example
Front of the business card will have the umbrella picture fading out just like the sample pdf with the image of the mask. The business card will be printed as a clear plastic just like the sample pdf of the mask so please fade it to a transparent design similar in size. I want the front to have just the words Lunar Orchard from my logo (not the logo itself) and the tagline: Web. Graphics. Print.
I'd like a similar design as the back of the mask business card in the sample pdf. It has to match the size of the design on the front. The logo can go at the top. Underneath, please use a similar icon system as in the pink sample pdf design. It will have my name 'Tessa Marwick', and 'Web. Graphics. Print' beside the contact icon. Under the phone icon, please insert my phone and email. Underneath, please place my website address. You can use your own icons or I can provide them. The colors are to be shades of blue from the umbrella, white, and the color from my logo. The purple business card design in the sample pdf is just for color variation and font ideas.
brovelmotion brovelmotion
Pls check your private messages
lOrchard lOrchard
Designs #1-6 is the best. Thank you for the other designs but I need it to look like the first 6.
Please put the umbrella picture on the front, fading into transparent edge like in the sample pdf. Please see instructions.

```html
<!DOCTYPE html>
<html lang="en">
<head>
<meta charset="utf-8">
<title>Lunar Orchard — Business Card</title>
<link rel="stylesheet" href="https://fonts.googleapis.com/css2?family=Exo+2:wght@700&family=Montserrat:wght@400;600&display=swap">
<style>
  :root {
    --page: #e9ecec;
    --card: #ffffff;
    --teal: #5cc3be;
    --teal-deep: #4bb5b0;
    --ink-light: #ffffff;
    --shadow: rgba(20, 40, 40, 0.18);
  }
  * { box-sizing: border-box; margin: 0; padding: 0; }
  html, body { width: 1200px; height: 899px; overflow: hidden; }
  body {
    background: var(--page);
    font-family: "Montserrat", sans-serif;
    display: flex;
    align-items: center;
    justify-content: center;
    gap: 48px;
  }
  .card {
    width: 520px;
    height: 300px;
    border-radius: 30px;
    background: var(--card);
    box-shadow: 0 14px 30px var(--shadow);
    overflow: hidden;
    position: relative;
    display: flex;
  }
  .brand {
    display: flex;
    flex-direction: column;
    align-items: center;
    gap: 14px;
  }
  .brand-mark {
    width: 46px;
    height: 46px;
    background: var(--teal);
  }
  .brand-name {
    font-family: "Exo 2", sans-serif;
    font-weight: 700;
    font-size: 26px;
    letter-spacing: 3px;
    color: var(--teal);
    text-transform: uppercase;
  }
  /* back side */
  .card-back .logo-half {
    width: 50%;
    display: flex;
    align-items: center;
    justify-content: center;
  }
  .card-back .logo-half .brand-name { font-size: 19px; letter-spacing: 2px; }
  .card-back .logo-half .brand-mark { width: 38px; height: 38px; }
  .details-half {
    width: 50%;
    background: var(--teal);
    color: var(--ink-light);
    padding: 34px 26px 26px 28px;
    display: flex;
    flex-direction: column;
    gap: 18px;
  }
  .person-name {
    font-weight: 600;
    font-size: 15px;
    letter-spacing: 1.5px;
    text-transform: uppercase;
  }
  .person-role {
    font-size: 10px;
    letter-spacing: 1px;
    margin-top: 4px;
    opacity: 0.9;
  }
  .address { font-size: 10px; line-height: 1.5; }
  .contact-list { list-style: none; display: flex; flex-direction: column; gap: 7px; }
  .contact-item {
    display: flex;
    align-items: center;
    gap: 8px;
    font-size: 9.5px;
  }
  .contact-icon { width: 12px; height: 12px; flex: none; }
  /* front side */
  .card-front {
    align-items: center;
    justify-content: center;
  }
</style>
</head>
<body>
  <section class="card card-back" aria-label="Card back">
    <div class="logo-half">
      <div class="brand">
        <span class="brand-mark"></span>
        <span class="brand-name">Lunar Orchard</span>
      </div>
    </div>
    <div class="details-half">
      <div class="person">
        <p class="person-name">Tessa Marwick</p>
        <p class="person-role">Creative Director</p>
      </div>
      <p class="address">24 Harbor Lane<br>Brookfield ST 04521</p>
      <ul class="contact-list">
        <li class="contact-item">
          <svg class="contact-icon" viewBox="0 0 24 24" fill="#fff"><path d="M6.6 10.8a15 15 0 0 0 6.6 6.6l2.2-2.2a1 1 0 0 1 1-.25 11.4 11.4 0 0 0 3.6.57 1 1 0 0 1 1 1V20a1 1 0 0 1-1 1A17 17 0 0 1 3 4a1 1 0 0 1 1-1h3.5a1 1 0 0 1 1 1c0 1.25.2 2.45.57 3.6a1 1 0 0 1-.25 1z"/></svg>
          <span>+0 555 014 2280</span>
        </li>
        <li class="contact-item">
          <svg class="contact-icon" viewBox="0 0 24 24" fill="none" stroke="#fff" stroke-width="2"><rect x="5" y="3" width="14" height="18" rx="2"/><line x1="10" y1="18" x2="14" y2="18"/></svg>
          <span>+0 555 014 2281</span>
        </li>
        <li class="contact-item">
          <svg class="contact-icon" viewBox="0 0 24 24" fill="none" stroke="#fff" stroke-width="2"><rect x="3" y="5" width="18" height="14" rx="1"/><path d="M3 6l9 7 9-7"/></svg>
          <span>tessa@lunarorchard.example</span>
        </li>
        <li class="contact-item">
          <svg class="contact-icon" viewBox="0 0 24 24" fill="none" stroke="#fff" stroke-width="2"><circle cx="12" cy="12" r="9"/><path d="M3 12h18M12 3c3 3 3 15 0 18M12 3c-3 3-3 15 0 18"/></svg>
          <span>www.lunarorchard.example</span>
        </li>
      </ul>
    </div>
  </section>

  <section class="card card-front" aria-label="Card front">
    <div class="brand">
      <span class="brand-mark"></span>
      <span class="brand-name">Lunar Orchard</span>
    </div>
  </section>
</body>
</html>
```